Energy Company needs a Business Card Design

We need a business card design for a new company based in Singapore called Kavu Energy. Kavu Energy is a producer of renewable energies largely for the biofuels market. Sourced entirely from sustainable resources, Kavu Energy aims to be a fully integrated oil company operating in 100% sustainable way. We would like to see designs that use the same colours as the attached file.

Industry/Entity Type

Business

```html
<!DOCTYPE html>
<html lang="en">
<head>
<meta charset="utf-8">
<title>Kavu Energy — Business Card</title>
<link rel="stylesheet" href="https://fonts.googleapis.com/css2?family=Questrial&display=swap">
<style>
  :root {
    --backdrop: #e4e4e4;
    --card-dark-top: #5a5a5a;
    --card-dark-bottom: #2f2f2f;
    --card-light: #ffffff;
    --brand-grey: #8a8a8a;
    --text-grey: #7a7a7a;
    --brand-green: #7dba3a;
  }
  * { margin: 0; padding: 0; box-sizing: border-box; }
  html, body {
    width: 1200px; height: 720px; overflow: hidden;
    background: var(--backdrop);
    font-family: "Questrial", "Century Gothic", sans-serif;
  }
  .canvas { position: relative; width: 1200px; height: 720px; }
  .card {
    position: absolute; top: 241px;
    width: 420px; height: 240px;
    border-radius: 2px;
  }
  .card--front {
    left: 147px;
    background: linear-gradient(160deg, var(--card-dark-top), var(--card-dark-bottom));
    display: flex; flex-direction: column; align-items: center; justify-content: center;
  }
  .card--back { left: 633px; background: var(--card-light); }

  .wordmark {
    display: flex; align-items: center; gap: 10px;
    color: var(--brand-grey);
  }
  .wordmark__dot {
    width: 14px; height: 14px; border-radius: 50%;
    background: var(--brand-green);
  }
  .wordmark__name { font-size: 44px; letter-spacing: 0.5px; }

  .tagline {
    margin-top: 22px;
    color: var(--brand-green);
    font-size: 15.5px; letter-spacing: 0.2px;
  }

  .contact-person { position: absolute; left: 21px; top: 66px; }
  .contact-person__name {
    color: var(--brand-green); font-size: 17px; font-weight: 700;
    -webkit-text-stroke: 0.3px var(--brand-green);
  }
  .contact-person__role { color: var(--text-grey); font-size: 13px; margin-top: 1px; }

  .contact-list { position: absolute; left: 19px; top: 118px; list-style: none; }
  .contact-list__item {
    display: flex; align-items: center; gap: 8px;
    color: var(--text-grey); font-size: 12px; height: 20px;
  }
  .contact-list__icon { width: 12px; height: 12px; flex: none; }

  .card--back .wordmark {
    position: absolute; right: 22px; top: 98px;
  }
  .card--back .wordmark__name { font-size: 28px; }
  .card--back .wordmark__dot { width: 10px; height: 10px; }
</style>
</head>
<body>
<main class="canvas">
  <section class="card card--front" aria-label="Card front">
    <div class="wordmark">
      <span class="wordmark__dot"></span>
      <span class="wordmark__name">Kavu Energy</span>
    </div>
    <p class="tagline">Energy for Biofuels Market</p>
  </section>

  <section class="card card--back" aria-label="Card back">
    <div class="contact-person">
      <p class="contact-person__name">Daniel Reyes</p>
      <p class="contact-person__role">CEO</p>
    </div>
    <ul class="contact-list">
      <li class="contact-list__item">
        <svg class="contact-list__icon" viewBox="0 0 12 12" aria-hidden="true">
          <rect x="3" y="0.5" width="6" height="11" rx="1" fill="none" stroke="var(--brand-green)" stroke-width="1.2"/>
          <rect x="5" y="9" width="2" height="1" fill="var(--brand-green)"/>
        </svg>
        <span>+ 65 555 0142</span>
      </li>
      <li class="contact-list__item">
        <svg class="contact-list__icon" viewBox="0 0 12 12" aria-hidden="true">
          <rect x="0.5" y="2.5" width="11" height="7.5" fill="var(--brand-green)"/>
          <path d="M0.8 2.8 L6 7 L11.2 2.8" fill="none" stroke="#fff" stroke-width="1"/>
        </svg>
        <span>hello@kavufuel.com</span>
      </li>
      <li class="contact-list__item">
        <svg class="contact-list__icon" viewBox="0 0 12 12" aria-hidden="true">
          <g fill="none" stroke="var(--brand-green)" stroke-width="0.9">
            <circle cx="6" cy="6" r="5.2"/>
            <ellipse cx="6" cy="6" rx="2.3" ry="5.2"/>
            <line x1="0.8" y1="6" x2="11.2" y2="6"/>
            <line x1="1.6" y1="3.4" x2="10.4" y2="3.4"/>
            <line x1="1.6" y1="8.6" x2="10.4" y2="8.6"/>
          </g>
        </svg>
        <span>www.kavuenergy.com</span>
      </li>
    </ul>
    <div class="wordmark">
      <span class="wordmark__dot"></span>
      <span class="wordmark__name">Kavu Energy</span>
    </div>
  </section>
</main>
</body>
</html>
```